Fundraiser Flyer and Email Template

We are looking for a flexible coordinated flyer and email template. The feel of both should be more formal or professional. We are not looking for an overly "political" design that features American flags or other "political" symbols.

We are a political fundraising firm that works with elected officials to set up fundraisers for their campaigns. We send the invites to these events via US Mail and email, so we are looking for a standardized template that will work as both an 8.5 x 11 inch printed flyer, as well as an email template.

The information in the email will be text, but images can be used for formatting.

Some clients have a campaign logo, others do not. The format should be flexible enough to either include the logo, or leave it out. Size also varies.

Any colors in the template should be editable so we can match logos as we get them.

We're open to any format that allows us to edit the format as needed. This would include Photoshop, Microsoft Word, etc.

The text of the invite should include space for:

---------------------------------------
NAME
DISTRICT NUMBER AND OFFICE

DATE OF EVENT
TIME OF EVENT

LOCATION
LOCATION ADDRESS
LOCATION CITY, STATE, ZIP

SUGGESTED CONTRIBUTION LEVELS (Typically 3 levels are provided such as Gold: $1,000, Silver: $500, Bronze: $250)

ADDRESS TO SEND CHECKS TO

RSVP CONTACT INFORMATION

The invite will also need fine-print at the bottom that reads:
"Pennsylvania law allows personal, partnership, and PAC contributions. By law we cannot accept corporate contributions
Paid for by [NAME]"

Industry/Entity Type

It Professional

Font styles to use
Serif
Sans Serif

Requirements
Must have
• Must have spaces for:
• NAME
• DISTRICT NUMBER AND OFFICE
• DATE OF EVENT
• TIME OF EVENT
• LOCATION
• LOCATION ADDRESS
• LOCATION CITY, STATE, ZIP
• SUGGESTED CONTRIBUTION LEVELS (Typically 3 levels are provided such as Gold: $1,000, Silver: $500, Bronze: $250)
• ADDRESS TO SEND CHECKS TO
• RSVP CONTACT INFORMATION
• The invite will also need fine-print at the bottom that reads:
• "Pennsylvania law allows personal, partnership, and PAC contributions. By law we cannot accept corporate contributions
• Paid for by [NAME]"
Should not have
• It should not be overly "political".

```html
<!DOCTYPE html>
<html lang="en">
<head>
<meta charset="utf-8">
<title>Annual Fundraiser Invitation</title>
<link rel="stylesheet" href="https://fonts.googleapis.com/css2?family=Montserrat:wght@400;600;700;800;900&family=Open+Sans:wght@400;600;700&family=Playfair+Display:ital@1&display=swap">
<style>
  :root {
    --backdrop: #e9e7e3;
    --paper: #ffffff;
    --blue-deep: #0e3378;
    --blue-mid: #1a4ba3;
    --blue-light: #2a63c4;
    --accent-red: #e3101e;
    --ink: #111111;
    --on-blue: #ffffff;
  }
  * { box-sizing: border-box; margin: 0; padding: 0; }
  html, body { width: 993px; height: 1200px; overflow: hidden; }
  body { background: var(--backdrop); font-family: "Open Sans", Arial, sans-serif; color: var(--ink); }

  .flyer {
    position: absolute; left: 46px; top: 18px;
    width: 900px; height: 1164px;
    background: var(--paper); overflow: hidden;
    box-shadow: 0 4px 18px rgba(0,0,0,0.15);
  }
  .header-shape { position: absolute; left: 0; top: 0; width: 900px; height: 720px; }

  .header-text { position: absolute; left: 0; top: 0; width: 900px; text-align: center; color: var(--on-blue); }
  .district {
    position: absolute; top: 62px; width: 100%;
    font-family: "Montserrat", Arial, sans-serif; font-weight: 400;
    font-size: 20px; letter-spacing: 2px; text-transform: uppercase;
  }
  .candidate-name {
    position: absolute; top: 100px; width: 100%;
    font-family: "Montserrat", Arial, sans-serif; font-weight: 900;
    font-size: 104px; line-height: 104px; text-transform: uppercase; letter-spacing: 1px;
  }
  .invite-line {
    position: absolute; top: 322px; width: 100%;
    font-family: "Playfair Display", Georgia, serif; font-style: italic; font-size: 28px;
  }
  .event-time {
    position: absolute; top: 378px; left: 190px; width: 520px; height: 112px;
    background: var(--accent-red); border-radius: 14px;
    font-family: "Montserrat", Arial, sans-serif; font-weight: 700;
    font-size: 30px; line-height: 40px; padding-top: 16px; text-transform: uppercase;
  }
  .venue {
    position: absolute; top: 512px; width: 100%;
    font-family: "Montserrat", Arial, sans-serif; font-weight: 700; font-size: 22px; text-transform: uppercase;
  }
  .venue-address {
    position: absolute; top: 546px; width: 100%;
    font-size: 20px; line-height: 30px;
  }

  .reply-form { position: absolute; left: 0; top: 730px; width: 900px; text-align: center; }
  .checkbox {
    display: inline-block; width: 20px; height: 20px; border: 2px solid var(--ink);
    vertical-align: -3px; margin-right: 8px;
  }
  .attend-line { font-weight: 700; font-size: 22px; }
  .attend-line .yes { font-size: 32px; font-weight: 700; }
  .attend-line .checkbox { width: 26px; height: 26px; vertical-align: -4px; }
  .levels { margin-top: 22px; font-size: 20px; }
  .levels .level { margin: 0 22px; }
  .levels strong { font-weight: 700; }
  .paid-by { margin-top: 26px; font-size: 20px; }
  .paid-by .fill-line { display: inline-block; width: 430px; border-bottom: 1.5px solid var(--ink); margin-left: 8px; }
  .rsvp {
    margin: 30px auto 0; width: 660px; height: 64px; line-height: 64px;
    background: var(--accent-red); color: var(--on-blue); border-radius: 12px;
    font-weight: 700; font-size: 25px;
  }
  .cheque-info { margin-top: 26px; font-size: 18px; line-height: 28px; }
  .fine-print { margin-top: 30px; font-size: 15px; line-height: 24px; }
</style>
</head>
<body>
  <main class="flyer">
    <svg class="header-shape" viewBox="0 0 900 720" aria-hidden="true">
      <defs>
        <radialGradient id="blueField" cx="0.3" cy="0.35" r="0.8">
          <stop offset="0" stop-color="var(--blue-light)"/>
          <stop offset="0.55" stop-color="var(--blue-mid)"/>
          <stop offset="1" stop-color="var(--blue-deep)"/>
        </radialGradient>
      </defs>
      <circle cx="380" cy="-120" r="826" fill="none" stroke="var(--accent-red)" stroke-width="8"/>
      <circle cx="380" cy="-120" r="800" fill="url(#blueField)"/>
      <circle cx="380" cy="-120" r="810" fill="none" stroke="var(--accent-red)" stroke-width="3"/>
    </svg>

    <header class="header-text">
      <p class="district">Harlow County - District 4</p>
      <h1 class="candidate-name">Marcus<br>Whitfield</h1>
      <p class="invite-line">Cordially invites you to our Annual Fundraiser</p>
      <p class="event-time">Thursday - June 11, 2016<br>6:00 - 8:00 PM</p>
      <p class="venue">Lantern Hall Gallery</p>
      <p class="venue-address">Oakridge Plaza, 4120 Meadow Lane Road,<br>Fairview, MD</p>
    </header>

    <section class="reply-form">
      <p class="attend-line"><span class="checkbox"></span><span class="yes">Yes!</span> I plan to attend, enclosed is my cheque for</p>
      <p class="levels">
        <span class="level"><span class="checkbox"></span><strong>Bronze:</strong> $250</span>
        <span class="level"><span class="checkbox"></span><strong>Silver:</strong> $500</span>
        <span class="level"><span class="checkbox"></span><strong>Gold:</strong> $1,000</span>
      </p>
      <p class="paid-by">Paid for by<span class="fill-line"></span></p>
      <p class="rsvp">Please RSVP by email: rsvp@whitfieldevents.com</p>
      <p class="cheque-info">Please make the cheque to: Marcus Whitfield, PO BOX 5120,<br>4120 Meadow Lane Road, Fairview, MD</p>
      <p class="fine-print">Pennsylvania law allows personal, partnership, and PAC contributions.<br>By law we cannot accept corporate contributions</p>
    </section>
  </main>
</body>
</html>
```